Lumo Sourdough Tortilla bag design front and back

Our tortilla bags are flat plastic bags. I would like a design for the front and back of our tortillas. Our tortillas are made of whole wheat flour. We have decided to go with the following font and color scheme for our tortilla bags from the updated attached samples below. Wheat or taco images are okay to brighten and make the package stand out. We prefer a clean look. We prefer the word "Artisian" to remain in cursive.

Target Market(s)

Health conscious consumers

Industry/Entity Type

Bakery

Font styles to use
Serif
Sans Serif
Decorative

Colors
59FF00
82FF00
B8FF75
E3FFCB
F4FFEA
EB3D1F
EC4F4E
F09395
F8D3D4
FCEDEE

Requirements
Must have
• The word "sourdough must standout and be prominent on the front,
Nice to have
• Looking for clean upscale look that pops

```html
<!DOCTYPE html>
<html lang="en">
<head>
<meta charset="UTF-8">
<title>Lumo Sourdough Artisan Tortilla – Bag Front</title>
<link rel="stylesheet" href="https://fonts.googleapis.com/css2?family=Bebas+Neue&family=Kaushan+Script&family=Libre+Baskerville:wght@400;700&family=Yellowtail&display=swap">
<style>
  :root {
    --backdrop: #c0d4fe;
    --bag-black: #1c1c1c;
    --bag-shade: #0e0e0e;
    --gold-dark: #c97a12;
    --gold-light: #ffd36b;
    --blush: #f8d3d4;
    --blush-ink: #2a1d1d;
    --white: #ffffff;
    --window-gold: #d79a2b;
  }
  * { margin: 0; padding: 0; box-sizing: border-box; }
  html, body { width: 1200px; height: 960px; overflow: hidden; }
  body { background: var(--backdrop); position: relative; }

  .bag {
    position: absolute; left: 388px; top: 208px;
    width: 424px; height: 600px;
    background: linear-gradient(90deg, var(--bag-shade) 0%, var(--bag-black) 12%, #262626 50%, var(--bag-black) 88%, var(--bag-shade) 100%);
    overflow: hidden;
  }
  .bag__top-seal {
    position: absolute; left: 0; top: 0; width: 100%; height: 56px;
    background: linear-gradient(90deg, var(--gold-dark) 0%, var(--gold-light) 25%, var(--gold-dark) 45%, var(--gold-light) 65%, var(--gold-dark) 100%);
  }
  .bag__top-edge { position: absolute; left: 0; top: 50px; width: 100%; height: 8px; }
  .bag__bottom-seal {
    position: absolute; left: 0; bottom: 0; width: 100%; height: 24px;
    background: #111; border-top: 1px solid #2e2e2e;
  }
  .brand-tab {
    position: absolute; left: 64px; top: 0; width: 78px; height: 110px;
    background: var(--blush); border-radius: 0 0 6px 6px;
    display: flex; align-items: flex-end; justify-content: center; padding-bottom: 18px;
  }
  .brand-tab__name {
    font-family: "Libre Baskerville", serif; font-weight: 700;
    font-size: 17px; color: var(--blush-ink); letter-spacing: 0;
  }
  .headline {
    position: absolute; left: 0; top: 136px; width: 100%; text-align: center;
    font-family: "Bebas Neue", sans-serif; font-size: 78px; line-height: 1;
    color: var(--white); letter-spacing: 1px;
  }
  .product-window {
    position: absolute; left: 70px; top: 212px; width: 298px; height: 106px;
    border: 3px solid var(--window-gold);
    background: linear-gradient(90deg, #e9e4da 0%, #d9e3c3 20%, #f0e6d8 40%, #dfe6c4 60%, #efe7dc 80%, #e3dccd 100%);
  }
  .subtitle-script {
    position: absolute; left: 0; top: 324px; width: 100%; text-align: center;
    font-family: "Kaushan Script", "Yellowtail", "Brush Script MT", cursive;
    font-size: 36px; line-height: 1.1; color: var(--white);
  }
  .subtitle {
    position: absolute; left: 0; top: 368px; width: 100%; text-align: center;
    font-family: "Bebas Neue", sans-serif; font-size: 74px; line-height: 1;
    color: var(--white); letter-spacing: 1px;
  }
  .rule {
    position: absolute; left: 108px; top: 437px; width: 228px; height: 1px;
    background: rgba(255,255,255,0.7);
  }
  .claims { position: absolute; left: 98px; top: 449px; }
  .keep-frozen {
    position: absolute; left: 260px; top: 458px; width: 164px; height: 44px;
    background: var(--blush);
    clip-path: polygon(14px 0, 100% 0, 100% 100%, 14px 100%, 0 50%);
    display: flex; align-items: center; justify-content: center; padding-left: 10px;
    font-family: "Libre Baskerville", serif; font-size: 18px; color: var(--blush-ink);
  }
  .count, .net-weight {
    position: absolute; left: 0; width: 100%; text-align: center;
    font-family: "Libre Baskerville", serif; font-weight: 700; color: var(--white);
    line-height: 1.2;
  }
  .count { top: 520px; font-size: 14px; }
  .net-weight { top: 543px; font-size: 12px; }
</style>
</head>
<body>
  <div class="bag">
    <div class="bag__top-seal"></div>
    <svg class="bag__top-edge" viewBox="0 0 424 8" preserveAspectRatio="none" aria-hidden="true">
      <polygon fill="#1c1c1c" points="0,8 0,4 4,0 8,4 12,0 16,4 20,0 24,4 28,0 32,4 36,0 40,4 44,0 48,4 52,0 56,4 60,0 64,4 68,0 72,4 76,0 80,4 84,0 88,4 92,0 96,4 100,0 104,4 108,0 112,4 116,0 120,4 124,0 128,4 132,0 136,4 140,0 144,4 148,0 152,4 156,0 160,4 164,0 168,4 172,0 176,4 180,0 184,4 188,0 192,4 196,0 200,4 204,0 208,4 212,0 216,4 220,0 224,4 228,0 232,4 236,0 240,4 244,0 248,4 252,0 256,4 260,0 264,4 268,0 272,4 276,0 280,4 284,0 288,4 292,0 296,4 300,0 304,4 308,0 312,4 316,0 320,4 324,0 328,4 332,0 336,4 340,0 344,4 348,0 352,4 356,0 360,4 364,0 368,4 372,0 376,4 380,0 384,4 388,0 392,4 396,0 400,4 404,0 408,4 412,0 416,4 420,0 424,4 424,8"/>
    </svg>

    <div class="brand-tab"><span class="brand-tab__name">LUMO</span></div>

    <h1 class="headline">SOURDOUGH</h1>

    <div class="product-window" role="img" aria-label="Window showing rolled tortilla wraps filled with lettuce, peppers and carrots"></div>

    <p class="subtitle-script">Artisan</p>
    <p class="subtitle">TORTILLA</p>
    <div class="rule"></div>

    <svg class="claims" width="160" height="56" viewBox="0 0 160 56" aria-hidden="true">
      <circle cx="24" cy="28" r="20" fill="none" stroke="#ffffff" stroke-width="1.5"/>
      <circle cx="84" cy="28" r="20" fill="none" stroke="#ffffff" stroke-width="1.5"/>
      <circle cx="84" cy="28" r="13" fill="#ffffff"/>
      <circle cx="144" cy="28" r="18" fill="none" stroke="#ffffff" stroke-width="1.5"/>
    </svg>

    <div class="keep-frozen">Keep Frozen</div>

    <p class="count">8CT</p>
    <p class="net-weight">Net Weight- 12 Ounces / 243G</p>

    <div class="bag__bottom-seal"></div>
  </div>
</body>
</html>
```